IT Company Business Card Rebranding

We want to modernize our business cards massively. We want to incorporate aspects of our old business card such as the white and geometric design with the blues of another icon. Existing Logo, old business card and icon are all attached.

We are a modern IT company that provides support for new and growing technologies and want our business cards to be modern yet professional.
Updates

Note: Do not use file ICON.png in design. This is just a design we like Added Wednesday, March 9, 2016

Industry/Entity Type

Information Technology

Contact Information for Business Card

Roughly 43 : 26 or 1075 x 650 px

Font styles to use
Serif

Colors
0492cd
3276b5
33a6d7
86cfc6
cfeae6
cee9f5
ffffff

Requirements
Must have
• Modern yet professional
Nice to have
• We would like to incorporate the blues of our existing logo and of the icon provided. Really like the design of the icon.
Should not have
• Too Decorative. Just simple and professional.
• Not have the circle icon, as it is a copyrighted icon, I just like the colors and the geometric design

```html
<!DOCTYPE html>
<html lang="en">
<head>
<meta charset="UTF-8">
<title>CoreShift IT – Business Card</title>
<link rel="stylesheet" href="https://fonts.googleapis.com/css2?family=Exo+2:wght@700&family=Roboto:wght@300;400&display=swap">
<style>
  :root {
    --page-bg: #e9edf2;
    --card-white: #ffffff;
    --blue-deep: #1f4fbf;
    --blue-mid: #3276b5;
    --blue-bright: #0492cd;
    --blue-light: #33a6d7;
    --name-blue: #2f6fd6;
    --swoosh-grey: #a9acb0;
    --text-grey: #5d6166;
    --brand-grey: #8c9096;
  }
  html, body {
    margin: 0;
    padding: 0;
    width: 1200px;
    height: 950px;
    overflow: hidden;
    background: var(--page-bg);
  }
  .canvas {
    position: relative;
    width: 1200px;
    height: 950px;
  }
  .card {
    position: absolute;
    left: 62px;
    top: 150px;
    width: 1075px;
    height: 650px;
    background: var(--card-white);
    overflow: hidden;
    box-shadow: 0 10px 30px rgba(20, 40, 80, 0.18);
  }
  .card-swoosh {
    position: absolute;
    inset: 0;
    width: 100%;
    height: 100%;
  }
  .brand {
    position: absolute;
    left: 110px;
    top: 300px;
    display: flex;
    align-items: center;
    gap: 18px;
  }
  .brand-dot {
    width: 22px;
    height: 22px;
    border-radius: 50%;
    background: var(--blue-mid);
  }
  .brand-name {
    font-family: "Roboto", sans-serif;
    font-weight: 300;
    font-size: 30px;
    letter-spacing: 9px;
    color: var(--brand-grey);
  }
  .contact-block {
    position: absolute;
    left: 560px;
    top: 130px;
  }
  .person-name {
    margin: 0;
    font-family: "Exo 2", sans-serif;
    font-weight: 700;
    font-size: 46px;
    line-height: 1.1;
    color: var(--name-blue);
  }
  .person-role {
    margin: 4px 0 30px;
    font-family: "Roboto", sans-serif;
    font-weight: 400;
    font-size: 26px;
    color: var(--text-grey);
  }
  .contact-list {
    list-style: none;
    margin: 0;
    padding: 0;
  }
  .contact-item {
    display: flex;
    align-items: center;
    gap: 14px;
    margin-bottom: 12px;
    font-family: "Roboto", sans-serif;
    font-weight: 400;
    font-size: 25px;
    color: var(--text-grey);
  }
  .contact-icon {
    width: 24px;
    height: 24px;
    flex: none;
    fill: var(--blue-mid);
  }
</style>
</head>
<body>
<main class="canvas">
  <section class="card" aria-label="Business card front">
    <svg class="card-swoosh" viewBox="0 0 1075 650" preserveAspectRatio="none" aria-hidden="true">
      <defs>
        <linearGradient id="swooshBlue" x1="0" y1="0" x2="1" y2="0">
          <stop offset="0" stop-color="#1f4fbf"/>
          <stop offset="0.55" stop-color="#0492cd"/>
          <stop offset="1" stop-color="#33a6d7"/>
        </linearGradient>
      </defs>
      <path class="swoosh-grey" d="M0,632 C250,540 650,420 1075,572 L1075,650 L0,650 Z" fill="var(--swoosh-grey)"/>
      <path class="swoosh-white-gap" d="M0,644 C250,552 650,434 1075,586 L1075,650 L0,650 Z" fill="#ffffff"/>
      <path class="swoosh-blue" d="M0,650 C250,560 650,446 1075,598 L1075,650 Z" fill="url(#swooshBlue)"/>
    </svg>

    <div class="brand">
      <span class="brand-dot"></span>
      <span class="brand-name">CORESHIFT IT</span>
    </div>

    <div class="contact-block">
      <h1 class="person-name">Daniel Reyes</h1>
      <p class="person-role">CEO/Founder</p>
      <ul class="contact-list">
        <li class="contact-item">
          <svg class="contact-icon" viewBox="0 0 24 24" aria-hidden="true"><path d="M6.6 10.8a15.1 15.1 0 0 0 6.6 6.6l2.2-2.2c.3-.3.7-.4 1-.2 1.1.4 2.3.6 3.6.6.6 0 1 .4 1 1V20c0 .6-.4 1-1 1A17 17 0 0 1 3 4c0-.6.4-1 1-1h3.5c.6 0 1 .4 1 1 0 1.3.2 2.5.6 3.6.1.3 0 .7-.2 1z"/></svg>
          <span>555 204 7816</span>
        </li>
        <li class="contact-item">
          <svg class="contact-icon" viewBox="0 0 24 24" aria-hidden="true"><path d="M3 5h18v14H3z M3 5l9 7 9-7" fill="none" stroke="var(--blue-mid)" stroke-width="2"/></svg>
          <span>hello@coreshift.com</span>
        </li>
        <li class="contact-item">
          <svg class="contact-icon" viewBox="0 0 24 24" aria-hidden="true"><circle cx="12" cy="12" r="10"/><path d="M2 12h20M12 2c3 3 3 17 0 20M12 2c-3 3-3 17 0 20" fill="none" stroke="#ffffff" stroke-width="1.4"/></svg>
          <span>www.coreshift.com</span>
        </li>
      </ul>
    </div>
  </section>
</main>
</body>
</html>
```